Hospital Website Design - PSD only

We need a web design for a community hospital based in Uniontown, Pennsylvania.

We would like to see a first round of designs for the website HOMEPAGE. Once we have selected finalists for the look & feel, based on the submitted homepage designs, we will request an additional INTERNAL page design.

Both designs should follow the content requirements displayed on the attached wireframes. I will post the internal page wireframe after the homepage design finalists are selected.

The desired Look & Feel for the website is clean and modern.

3 sites we like are:
http://www.larkfieldcare.org/
http://www.qmtc.org/
http://www.vendrel.org/

Attached are the Homepage wireframe, and the Marbrook Hospital Logo.

The winning design will communicate a bright, healthy, energetic, community-oriented feeling.

Please note that readability is very important for a hospital website. Font-sizes and line-heights should be carefully selected for comfortable reading.
Updates

Dear designers -- Please don't feel locked into the exact shades of blue / brown used in the logo. We find this color scheme quite ugly and are working on a logo update. The new color scheme will probably still involve some shades of blue and brown, but we aren't sure yet. Please use your best judgement to make a beautiful design, similar in style to the modern / simple aesthetic of http://www.larkfieldcare.org/ We will be working on feedback to designs today. Thank you.

Regarding Large Rotating Graphic area and Navigation: We prefer a full-width display, rather than boxed. The navigation should be visually prominent, easy to read text that one can scan easily across the top of the page. Again, please refer to http://www.larkfieldcare.org/ for our preferred design aesthetic. Some of the designs submitted have been somewhat dated in their styling. We'd like a polished, modern, crisp, bold, beautiful design.

Re: choice of image in large rotating graphic area -- Designers, please do not use stock photography of a group of doctors, or a nursing home scene, in your sample rotating graphic areas. Although this should not affect our perception of the design, it throws off everything in the page if we don't like the image. Please try to select a bold / attractive image that you would like to set the tone for your design.

Reason: Extending our deadline to receive more designs exploring other color options containing less brown, or browns with a more attractive vibe. We would also like to see designs that are not exact replicas of the wireframe. The wireframe is just to show the elements on the page. Please use your creativity to utilize these elements in an attractive layout that we will like. We would also prefer to see use of photography that shows a younger, more cheerful, hopeful feeling in the design... and where the photographs are consistent with your design approach. Thanks!

In general, feedback for everyone is, please look here: http://www.larkfieldcare.org/ that's the feeling / vibe we want. DO NOT let the old, ugly, outdated logo determine your design. We are having the logo redesigned. DO NOT take an ugly, outdated template, and adapt it for this website. We want to see something BEAUTIFUL!!! Please give us your best effort! People who come to this website are in health crisis, and they want to be uplifted!! Their good spirits are in your hands.

Reason: We are still reviewing submissions and working with designers to provide better feedback. Thanks for your patience.

Reason: our sincerest apologies for the failure to provide adequate feedback this week. We hit a snag with the various decision makers on this project and were not able to review the recent submissions. We will make every effort to have a decision by tomorrow. Thank you for your patience.

Target Market(s)

Adults based in suburban & rural community, aged 18-80.

Industry/Entity Type

Hospital

Requirements
Must have
• The design must include all of the content areas outlined on the attached wireframe.
The design must include the attached logo. (Note, we may update the logo during the design contest, but it will not be changed dramatically. It will just be modernized slightly.)
Nice to have
• Show hover states for things like Navigation, Links, or small images in gallery, so we can see how you imagine interactive states.

```html
<!DOCTYPE html>
<html lang="en">
<head>
<meta charset="utf-8">
<title>Marbrook Hospital</title>
<link href="https://fonts.googleapis.com/css2?family=Open+Sans:wght@400;600;700&family=Libre+Baskerville&display=swap" rel="stylesheet">
<style>
:root{
  --brown:#8a6a3b;
  --brown-dark:#6f5229;
  --blue:#0b4fa3;
  --blue-deep:#0a3f88;
  --text:#333;
  --muted:#555;
  --line:#dcdcdc;
  --panel:#f3f3f3;
}
*{box-sizing:border-box;margin:0;padding:0}
html,body{width:1078px;height:1200px;overflow:hidden}
body{position:relative;font-family:"Open Sans",Arial,sans-serif;color:var(--text);background:#fff}
a{color:inherit;text-decoration:none}
.abs{position:absolute}

.topbar{left:0;top:0;width:1078px;height:24px;background:var(--brown);color:#fff;font-size:13px}
.topbar .call{left:104px;top:3px;display:flex;align-items:center;gap:6px}
.topbar .contact{left:250px;top:3px;text-decoration:underline}
.topbar .tools{left:848px;top:3px;display:flex;gap:12px;align-items:center}
.lang{left:908px;top:0;width:67px;height:31px;background:#a58a5e;color:#fff;font-size:13px;text-align:center;line-height:28px;clip-path:polygon(0 0,100% 0,100% 85%,50% 100%,0 85%)}

.brand{left:103px;top:62px;font-size:21px;font-weight:600;color:var(--blue);letter-spacing:.5px;display:flex;align-items:center;gap:8px}
.brand .dot{width:12px;height:12px;border-radius:50%;background:var(--brown)}
.util{left:572px;top:86px;display:flex;gap:24px;font-size:12px;color:#333}
.site-search{left:767px;top:73px;display:flex}
.site-search .field{width:148px;height:25px;border:1px solid #ccc;font-size:8px;color:#aaa;padding:7px 9px}
.btn{background:var(--brown);color:#fff;font-size:9px;display:flex;align-items:center;justify-content:center}
.site-search .btn{width:60px;height:25px}

.mainnav{left:0;top:111px;width:1078px;height:32px;background:var(--blue);color:#fff;font-size:12.5px;font-weight:600}
.mainnav ul{list-style:none;display:flex;position:absolute;left:128px;top:8px}
.mainnav li{margin-right:38px}

.hero-bg{left:0;top:143px;width:1078px;height:325px;background:linear-gradient(#e8e8e8,#f6f6f6)}
.hero{left:103px;top:143px;width:872px;height:278px;background:linear-gradient(90deg,#6b6a30 0%,#8a7a45 30%,#7e5a35 42%,#4d5e2c 45%,#c79b80 65%,#8f8a86 100%)}
.hero h1{position:absolute;left:22px;top:58px;font-family:"Libre Baskerville",Georgia,serif;font-weight:400;color:#fff;font-size:33px;text-shadow:0 2px 4px rgba(0,0,0,.5)}
.hero p{position:absolute;left:31px;top:116px;width:320px;font-family:"Libre Baskerville",Georgia,serif;color:#fff;font-size:26px;line-height:32px;text-shadow:0 2px 4px rgba(0,0,0,.5)}
.arrow{top:245px}

.quickbar{left:103px;top:421px;width:872px;height:78px;background:#fff;border:1px solid #e2e2e2;box-shadow:0 10px 12px -6px rgba(0,0,0,.25)}
.condition{position:absolute;left:16px;top:14px;font-size:12.5px;font-weight:600}
.condition .row{display:flex;margin-top:6px}
.condition .field{width:174px;height:25px;border:1px solid #ccc;font-size:8px;color:#aaa;padding:7px 9px;font-weight:400}
.condition .btn{width:59px;height:25px;font-weight:400}
.qlink{position:absolute;top:0;height:78px;display:flex;align-items:center;gap:10px;font-size:12.5px;line-height:14px;color:#333}
.sep{position:absolute;top:0;width:16px;height:78px}

.box{border:1px solid #d8d8d8;background:linear-gradient(#fff,var(--panel))}
.box h3{font-size:12.5px;font-weight:700;color:var(--blue);text-transform:uppercase}
.media{left:103px;top:540px;width:428px;height:237px}
.media h3{text-transform:none}
.gallery-grid{position:absolute;left:8px;top:36px;display:grid;grid-template-columns:repeat(3,62px);gap:8px 8px;column-gap:8px}
.thumb{width:62px;height:52px;border:1px solid #ccc;background:#fff;padding:3px}
.thumb div{width:100%;height:100%}
.thumb.active{border:2px solid var(--blue)}
.smalllink{position:absolute;font-size:10px;color:var(--brown)}
.video{position:absolute;left:221px;top:36px;width:198px;height:154px;background:linear-gradient(120deg,#5c6e78,#3a3230 55%,#2a2624)}
.video .ctrl{position:absolute;left:0;bottom:0;width:100%;height:14px;background:#1d1d1d}
.visit{left:539px;top:540px;width:214px;height:237px}
.list{list-style:none;font-size:11.5px;color:#444}
.list li{display:flex;gap:7px;align-items:flex-start}
.list li::before{content:"";flex:none;width:5px;height:5px;border:1.5px solid var(--blue);border-radius:50%;margin-top:4px}
.portal{left:761px;top:540px;width:214px;height:61px}
.resources{left:761px;top:612px;width:214px;height:165px}
.rule{position:absolute;left:9px;right:9px;height:1px;background:#ddd}

.tabs{left:103px;top:817px;width:872px;height:24px;border-bottom:1px dashed #aaa;font-size:12px;font-weight:700;color:var(--blue)}
.tabs span{position:absolute;top:0}
.tabs .on{left:0;padding:0 2px 4px;border-bottom:3px solid var(--brown)}
.story{position:absolute;top:867px;width:158px}
.story .pic{width:158px;height:134px;border:4px solid #d2d2d2}
.story.on .pic{border-color:var(--blue)}
.story .pic div{width:100%;height:100%}
.story p{margin-top:12px;font-size:11px;line-height:13px;color:#333}
.viewall{left:103px;top:1087px;font-size:12.5px;font-weight:700;color:var(--brown)}

.footer{left:0;top:1127px;width:1078px;height:73px;background:var(--blue);color:#fff}
.footer nav{position:absolute;left:110px;top:12px;display:flex;gap:23px;font-size:12.5px;font-weight:600}
.footer .copy{position:absolute;left:110px;top:41px;font-size:11.5px}
.footer .follow{position:absolute;left:501px;top:36px;display:flex;align-items:center;gap:6px;font-size:11.5px}
.follow i{display:block;width:20px;height:20px;border-radius:50%;background:#1a2d52}
.awards{position:absolute;left:818px;top:17px}
</style>
</head>
<body>

<div class="abs topbar">
  <div class="abs call"><svg width="11" height="12" viewBox="0 0 11 12"><path d="M2 1l2 0 1 3-1.5 1c.6 1.4 1.6 2.4 3 3L7.5 6.5l3 1v2C10 11 8 11.5 5 9S.5 3.5 2 1z" fill="#fff"/></svg>Call : 555- 010-4820</div>
  <a class="abs contact" href="#">CONTACT US</a>
  <div class="abs tools">
    <svg width="13" height="12" viewBox="0 0 13 12"><rect x="3" y="0" width="7" height="4" fill="#fff"/><rect x="0" y="4" width="13" height="5" rx="1" fill="#fff"/><rect x="3" y="8" width="7" height="4" fill="#fff" stroke="#8a6a3b"/></svg>
    <span style="font-size:11px;font-weight:600"><span style="font-size:8px">A</span>A<span style="font-size:13px">A</span></span>
  </div>
</div>
<div class="abs lang">Espanol</div>

<div class="abs brand"><span class="dot"></span>MARBROOK HOSPITAL</div>
<nav class="abs util"><a href="#">ABOUT US</a><a href="#">NEWS</a><a href="#">GIVING</a></nav>
<form class="abs site-search"><div class="field">Type your keywords...</div><div class="btn">Search</div></form>

<nav class="abs mainnav"><ul>
  <li>OUR SERVICES</li><li>FACILITIES &amp; DIRECTIONS</li><li>PATIENT &amp; VISITOR</li><li>INFORMATION</li><li>FIND A DOCTOR</li><li>HEALTH &amp; WELLNESS</li>
</ul></nav>

<div class="abs hero-bg"></div>
<svg class="abs arrow" style="left:68px" width="28" height="78" viewBox="0 0 28 78"><path d="M27 0L0 39 27 78 20 39z" fill="#c8c8c8"/></svg>
<svg class="abs arrow" style="left:983px" width="28" height="78" viewBox="0 0 28 78"><path d="M1 0l27 39L1 78 8 39z" fill="#c8c8c8"/></svg>
<section class="abs hero" role="img" aria-label="Photo: a young woman in recovery, looking hopeful, outdoors among greenery">
  <h1>Cancer Care Center</h1>
  <p>The Best Doctors And Nurses, And Treatment Close To Home.</p>
</section>

<div class="abs quickbar">
  <div class="condition">Do you want to learn about a condition?
    <div class="row"><div class="field">Diabetes, Cancer, Heart Health, ...</div><div class="btn">Search</div></div>
  </div>
  <svg class="sep" style="left:264px" viewBox="0 0 16 78"><path d="M1 0l14 39L1 78" fill="none" stroke="#e2e2e2" stroke-width="2"/></svg>
  <div class="qlink" style="left:298px"><svg width="36" height="34" viewBox="0 0 36 34"><path d="M12 0h12v11h12v12H24v11H12V23H0V11h12z" fill="var(--blue)"/><path d="M10 17l6 6 10-12" fill="none" stroke="#fff" stroke-width="3"/></svg>Symptom<br>Checker</div>
  <svg class="sep" style="left:414px" viewBox="0 0 16 78"><path d="M1 0l14 39L1 78" fill="none" stroke="#e2e2e2" stroke-width="2"/></svg>
  <div class="qlink" style="left:446px"><svg width="40" height="34" viewBox="0 0 40 34"><path d="M20 0h6v12l12 22H8l12-22z" fill="var(--blue)"/><path d="M6 14c-3 5-4 7-4 9a4 4 0 008 0c0-2-1-4-4-9z" fill="var(--blue)"/></svg>Schedule a<br>Lab Test</div>
  <svg class="sep" style="left:574px" viewBox="0 0 16 78"><path d="M1 0l14 39L1 78" fill="none" stroke="#e2e2e2" stroke-width="2"/></svg>
  <div class="qlink" style="left:604px"><svg width="36" height="36" viewBox="0 0 36 36"><circle cx="16" cy="16" r="14" fill="none" stroke="var(--blue)" stroke-width="3"/><circle cx="16" cy="16" r="8" fill="none" stroke="var(--blue)" stroke-width="3"/><path d="M16 16l6 18 3-6 6 6 3-3-6-6 6-3z" fill="var(--blue)" stroke="#fff"/></svg>Online Bill</div>
  <svg class="sep" style="left:722px" viewBox="0 0 16 78"><path d="M1 0l14 39L1 78" fill="none" stroke="#e2e2e2" stroke-width="2"/></svg>
  <div class="qlink" style="left:752px"><svg width="38" height="32" viewBox="0 0 38 32"><ellipse cx="15" cy="12" rx="14" ry="11" fill="var(--blue)"/><path d="M5 20l-3 8 9-5z" fill="var(--blue)"/><ellipse cx="26" cy="19" rx="11" ry="9" fill="var(--blue)" stroke="#fff" stroke-width="2"/><path d="M33 25l3 6-8-3z" fill="var(--blue)"/></svg>Support<br>Our Work</div>
</div>

<section class="abs box media">
  <h3 class="abs" style="left:9px;top:6px">Gallery</h3>
  <h3 class="abs" style="left:220px;top:6px">View Video</h3>
  <div class="rule" style="top:27px;right:218px"></div>
  <div class="rule" style="top:27px;left:221px"></div>
  <div class="gallery-grid">
    <div class="thumb active"><div role="img" aria-label="Gallery photo: doctor with patient" style="background:linear-gradient(#cfe0ee,#9ab6cc)"></div></div>
    <div class="thumb"><div role="img" aria-label="Gallery photo: medical team" style="background:linear-gradient(#f1eeea,#c9c2b8)"></div></div>
    <div class="thumb"><div role="img" aria-label="Gallery photo: scan room" style="background:linear-gradient(#bcd5c2,#6d8f71)"></div></div>
    <div class="thumb"><div role="img" aria-label="Gallery photo: doctor and patient" style="background:linear-gradient(#e6e2de,#c3b3a3)"></div></div>
    <div class="thumb"><div role="img" aria-label="Gallery photo: consultation" style="background:linear-gradient(#e8c7c0,#b7948c)"></div></div>
    <div class="thumb"><div role="img" aria-label="Gallery photo: care visit" style="background:linear-gradient(#ddd6d0,#a79a8d)"></div></div>
    <div class="thumb"><div role="img" aria-label="Gallery photo: nurse with patient" style="background:linear-gradient(#eadbd5,#b9968d)"></div></div>
    <div class="thumb"><div role="img" aria-label="Gallery photo: bedside care" style="background:linear-gradient(#e7eef3,#a9bfcf)"></div></div>
    <div class="thumb"><div role="img" aria-label="Gallery photo: doctor portrait" style="background:linear-gradient(#f1ece6,#c8b9a8)"></div></div>
  </div>
  <a class="smalllink" style="left:157px;top:215px" href="#">Thumbnails</a>
  <div class="video" role="img" aria-label="Video still: a presenter speaking by a harbour">
    <svg class="abs" style="left:86px;top:56px" width="26" height="18" viewBox="0 0 26 18"><rect width="26" height="18" rx="3" fill="#111" opacity=".8"/><path d="M10 4l7 5-7 5z" fill="#fff"/></svg>
    <div class="ctrl"></div>
  </div>
  <a class="smalllink" style="left:328px;top:215px" href="#">Subscribe to videos</a>
</section>

<section class="abs box visit">
  <h3 class="abs" style="left:9px;top:7px">About Your Visit</h3>
  <div class="rule" style="top:25px"></div>
  <ul class="list abs" style="left:11px;top:33px;line-height:20px">
    <li>Emergency Care</li><li>Accepted Health Plans</li><li>Pre-registration for Surgery</li><li>Lab Hours</li><li>Schedule a Lab Test</li><li>Find a Phone Number</li><li>Find a Form</li><li>Pay Bill Online</li><li>Visitor Guide</li>
  </ul>
  <a class="smalllink" style="left:151px;top:213px" href="#">Read More</a>
</section>

<section class="abs box portal">
  <h3 class="abs" style="left:9px;top:7px">Marbrook Patient Portal</h3>
  <div class="rule" style="top:25px"></div>
  <div class="abs btn" style="left:21px;top:33px;width:56px;height:20px;font-size:12px">Login</div>
  <span class="abs" style="left:88px;top:34px;font-size:12px">or</span>
  <div class="abs btn" style="left:113px;top:33px;width:64px;height:20px;font-size:12px">Register</div>
</section>

<section class="abs box resources">
  <h3 class="abs" style="left:9px;top:8px">Patient Resources</h3>
  <div class="rule" style="top:25px"></div>
  <ul class="list abs" style="left:11px;top:34px;width:190px;line-height:13px">
    <li style="margin-bottom:6px">Tips on Choosing the Right Doctor</li>
    <li style="margin-bottom:6px">Billing, Forms, &amp; Medical Records</li>
    <li>Making the Most of Your Appointment Hassle-Free Rx Refills</li>
  </ul>
  <a class="smalllink" style="left:151px;top:141px" href="#">Read More</a>
</section>

<div class="abs tabs"><span class="on">MH NEWS</span><span style="left:82px">UPCOMING CLASSES &amp; EVENTS</span></div>

<article class="story on" style="left:103px"><div class="pic"><div role="img" aria-label="Photo: doctor with an elderly patient" style="background:linear-gradient(#dfe8ef,#b9c9d5)"></div></div><p>Lorem ipsum dorel Lorema sitamet,consectetur Ipiscing elitr LoreNulla eulr Loremr sitamet,consectetur.</p></article>
<article class="story" style="left:281px"><div class="pic"><div role="img" aria-label="Photo: patient in a hospital bed with a doctor" style="background:linear-gradient(#c8d9ea,#8fa7bd)"></div></div><p>Lorem ipsum dorel Lorema sitamet,consectetur Ipiscing elitr LoreNulla eulr Loremr sitamet,consectetur.</p></article>
<article class="story" style="left:459px"><div class="pic"><div role="img" aria-label="Photo: hospital care team" style="background:linear-gradient(#f3f3f3,#d4d0cb)"></div></div><p>Lorem ipsum dorel Lorema sitamet,consectetur Ipiscing elitr LoreNulla eulr Loremr sitamet,consectetur.</p></article>
<article class="story" style="left:637px"><div class="pic"><div role="img" aria-label="Photo: hands holding an awareness ribbon" style="background:linear-gradient(#f4e7e4,#e4b8ad)"></div></div><p>Lorem ipsum dorel Lorema sitamet,consectetur Ipiscing elitr LoreNulla eulr Loremr sitamet,consectetur.</p></article>
<article class="story" style="left:816px"><div class="pic"><div role="img" aria-label="Photo: nurse caring for a patient" style="background:linear-gradient(#e7e3e1,#b6b8c2)"></div></div><p>Lorem ipsum dorel Lorema sitamet,consectetur Ipiscing elitr LoreNulla eulr Loremr sitamet,consectetur.</p></article>

<a class="abs viewall" href="#">View All Stories</a>

<footer class="abs footer">
  <nav><a href="#">Referring Physicians</a><a href="#">Medical Professionals</a><a href="#">Giving</a><a href="#">Volunteering</a><a href="#">Careers</a><a href="#">Online Bill Pay</a></nav>
  <div class="copy">Copyright 2014 MarbrookHospital&nbsp; All Rights Reserved</div>
  <div class="follow">Follow Us On&nbsp;<i></i><i></i><i></i><i></i><i></i></div>
  <svg class="awards" width="157" height="34" viewBox="0 0 157 34">
    <path d="M0 6h14v24H0l6-12z" fill="#5c4320"/>
    <path d="M157 6h-14v24h14l-6-12z" fill="#5c4320"/>
    <rect x="10" y="1" width="137" height="29" fill="var(--brown)"/>
    <text x="78.5" y="22" text-anchor="middle" fill="#fff" font-family="Open Sans, Arial, sans-serif" font-weight="700" font-size="16">AWARDS</text>
  </svg>
</footer>

</body>
</html>
```